Asia based real estate financing firm needs and AWESOME design for a biz card -Harborline Lending Partners

Looking for a stylish, & corporate-looking business card for a real estate financing brokerage firm in Asia, offering global mortgage loans. I uploaded our current logos. We would like to add a splash of color (perhaps the house icon) or any other suggestions are open. For the winning designer, we have a lot of work! Thanks and best of luck!

Target Market(s)

Real estate investors globally. We want to look more like a BANK and NOT a real estate company. Please don't play up on a "house" design.

Industry/Entity Type

Banking

Contact Information for Business Card

Harborline Lending Partners
Peter Walsh
Co-Founder | Partner

42 Kelvin Street, Suite 310
Singapore 074219
www.hlp-lend.example
peterwalsh@hlp-lend.example
+65 555-0147
WeChat: peterwalsh

Colors

Designer to choose colors to be used in the design.

Requirements
Must have
• Must have the standard business requirements for a card; name, address, email, etc
• Can be horizontal or vertical.
Nice to have
• It would be great to see some sort of variation to the logo with a pop of color. Red is good as we're in Asia, however, other options work as well.
• Our tag line is - Lending Without Limits. It doesn't have to be on the card but might be nice.
• I'd like to start seeing our tagline within the cards as well. - Lending Without Limits.
• Also, please add our location. The location for this card is Singapore so perhaps it can be highlighted or emphasised in some way.
• Singapore | Hong Kong | Shanghai | Manila
• As we will soon open an office in Shanghai, having an option for both languages would be great.
Should not have
• I'm exceited and open to your creativity ... knock it out of the park!

```html
<!DOCTYPE html>
<html lang="en">
<head>
<meta charset="utf-8">
<title>Harborline Lending Partners – Business Card</title>
<link rel="stylesheet" href="https://fonts.googleapis.com/css2?family=Roboto:wght@400;500;700&display=swap">
<style>
  :root {
    --navy: #1f3284;
    --navy-deep: #18286d;
    --navy-soft: #2c4196;
    --ink: #1c1c22;
    --paper: #ffffff;
    --paper-shade: #eef0f4;
    --backdrop: #c9cbcf;
  }
  * { margin: 0; padding: 0; box-sizing: border-box; }
  html, body { width: 1200px; height: 800px; overflow: hidden; }
  body {
    background: var(--backdrop);
    font-family: "Roboto", Arial, sans-serif;
    color: var(--ink);
    position: relative;
  }
  .card {
    position: absolute;
    left: 300px;
    width: 600px;
    height: 343px;
    box-shadow: 0 6px 18px rgba(0,0,0,0.22);
    overflow: hidden;
  }
  .card--back { top: 28px; background: var(--navy); }
  .card--front {
    top: 410px;
    background: linear-gradient(135deg, var(--paper) 0%, var(--paper) 60%, var(--paper-shade) 100%);
  }

  /* back */
  .back-pattern {
    position: absolute; inset: 0;
    background: linear-gradient(120deg, var(--navy-soft) 0%, var(--navy) 45%, var(--navy-deep) 100%);
  }
  .tagline {
    position: absolute;
    left: 44px; bottom: 40px;
    display: flex; align-items: center; gap: 12px;
    color: #fff;
    font-size: 15px; font-weight: 500;
    letter-spacing: 3px;
  }
  .tagline-mark { width: 14px; height: 14px; background: #fff; }

  /* front */
  .brand {
    position: absolute;
    left: 40px; top: 44px;
    color: var(--navy);
    font-size: 24px; font-weight: 500;
    letter-spacing: 0.5px;
    line-height: 1.2;
    width: 300px;
  }
  .address {
    position: absolute;
    left: 40px; top: 142px;
    font-size: 16px; line-height: 1.2;
    font-style: normal;
  }
  .contacts {
    position: absolute;
    left: 40px; top: 198px;
    list-style: none;
    font-size: 16px; line-height: 1.3;
  }
  .contacts li { display: flex; align-items: center; gap: 8px; }
  .contacts svg { width: 13px; height: 13px; fill: var(--navy); flex: none; }
  .person {
    position: absolute;
    right: 68px; top: 140px;
    text-align: right;
  }
  .person-name { color: var(--navy); font-size: 24px; font-weight: 700; }
  .person-role { font-size: 17px; margin-top: 2px; }
  .offices {
    position: absolute;
    top: 0; right: 0; bottom: 0;
    width: 36px;
    background: var(--navy);
    display: flex; align-items: center; justify-content: center;
  }
  .offices span {
    transform: rotate(-90deg);
    white-space: nowrap;
    color: #fff;
    font-size: 16px;
  }
  .offices strong { font-weight: 700; }
</style>
</head>
<body>

<section class="card card--back">
  <div class="back-pattern" role="img" aria-label="Repeating pattern of small embossed brand symbols across the navy card back"></div>
  <p class="tagline"><span class="tagline-mark"></span>Lending Without Limits</p>
</section>

<section class="card card--front">
  <h1 class="brand">Harborline Lending Partners</h1>

  <address class="address">
    42 Kelvin Street, Suite 310<br>Singapore 074219
  </address>

  <ul class="contacts">
    <li>
      <svg viewBox="0 0 16 16"><path d="M3.6 1.2l2.3 2.6-1.3 2a9 9 0 0 0 5.6 5.6l2-1.3 2.6 2.3-1.2 2.3C8 14.6 1.4 8 .9 2.4z"/></svg>
      +65 555-0147
    </li>
    <li>
      <svg viewBox="0 0 16 16"><circle cx="8" cy="8" r="7"/></svg>
      peterwalsh
    </li>
    <li>
      <svg viewBox="0 0 16 16"><path d="M1 3h14v10H1zm1.5 1.5v.4L8 8.6l5.5-3.7v-.4zm0 2.2v4.8h11V6.7L8 10.4z"/></svg>
      peterwalsh@hlp-lend.example
    </li>
    <li>
      <svg viewBox="0 0 16 16"><path d="M8 1a7 7 0 1 0 0 14A7 7 0 0 0 8 1zm0 1.4c.8.9 1.4 2.3 1.6 3.8H6.4C6.6 4.7 7.2 3.3 8 2.4zM2.5 7.5h2.5c0 1.5.2 2.8.7 4A5.6 5.6 0 0 1 2.5 7.5zm3.9 0h3.2c0 1.5-.6 3.1-1.6 4.1-1-1-1.6-2.6-1.6-4.1zm4.6 0h2.5a5.6 5.6 0 0 1-3.2 4c.5-1.2.7-2.5.7-4zM4.6 2.6c-.4 1-.6 2.2-.6 3.6H2.5a5.6 5.6 0 0 1 2.1-3.6zm6.8 0a5.6 5.6 0 0 1 2.1 3.6H12c0-1.4-.2-2.6-.6-3.6z"/></svg>
      www.hlp-lend.example
    </li>
  </ul>

  <div class="person">
    <p class="person-name">Peter Walsh</p>
    <p class="person-role">Co-Founder | Partner</p>
  </div>

  <aside class="offices">
    <span><strong>Singapore</strong> | Hong Kong | Shanghai | Manila</span>
  </aside>
</section>

</body>
</html>
```